Willowbend Pharmacy Business Cards

I need a business card design and or template. Needs to convey a softer feel along with health and wellness. Please see attached logo and color scheme.

Industry/Entity Type

Pharmacy

Colors

Designer to choose colors to be used in the design.

Requirements
Must have
• I've added a second NEW colored logo I think I am going to go with the blue green logo.
• Needs to have the colors and feel of the logo attached.
• Dorian Kessel
• Pharmacy Manager
• willowbendpharmacy.example

```html
<!DOCTYPE html>
<html lang="en">
<head>
<meta charset="utf-8">
<title>Willowbend Pharmacy – Business Cards</title>
<link rel="stylesheet" href="https://fonts.googleapis.com/css2?family=Josefin+Sans:wght@600&family=Roboto:wght@400&family=Roboto+Condensed:wght@500&display=swap">
<style>
  :root {
    --backdrop: #2b2b2b;
    --card: #f4f4f4;
    --ink: #5f6368;
    --text: #4d4d4d;
    --blue: #2fa3d8;
    --green: #93c23c;
  }
  * { margin: 0; padding: 0; box-sizing: border-box; }
  html, body { width: 1200px; height: 960px; overflow: hidden; }
  body { background: var(--backdrop); position: relative; }

  .card {
    position: absolute;
    width: 600px; height: 342px;
    background: var(--card);
    border-radius: 20px;
  }
  .card--front { left: 314px; top: 113px; }
  .card--back  { left: 311px; top: 472px; }

  .brand-dot { position: absolute; border-radius: 50%; background: var(--blue); }
  .brand-name {
    position: absolute;
    font-family: "Josefin Sans", sans-serif;
    font-weight: 600;
    color: var(--ink);
    white-space: nowrap;
    line-height: 1;
  }

  .card--front .brand-dot { left: 44px; top: 62px; width: 40px; height: 40px; }
  .card--front .brand-name { right: 40px; top: 62px; font-size: 32px; }
  .brand-rule {
    position: absolute; left: 42px; top: 106px;
    width: 390px; height: 2px; background: var(--green);
  }

  .contact-list {
    position: absolute; left: 40px; top: 208px;
    list-style: none;
    font-family: "Roboto", sans-serif;
    font-size: 14px; color: var(--text);
  }
  .contact-list li { display: flex; align-items: center; height: 19px; }
  .contact-list svg { width: 13px; height: 13px; margin-right: 10px; fill: var(--blue); flex: none; }

  .person {
    position: absolute; right: 43px; top: 248px; text-align: right;
    font-family: "Roboto Condensed", sans-serif; font-weight: 500;
    text-transform: uppercase; line-height: 1;
  }
  .person__name { color: var(--blue); font-size: 21px; }
  .person__title { color: var(--green); font-size: 15px; margin-top: 4px; letter-spacing: 0.2px; }

  .card--back .brand-dot { left: 130px; top: 148px; width: 52px; height: 52px; }
  .card--back .brand-name { left: 200px; top: 158px; font-size: 36px; }
  .card--back .brand-rule { left: 234px; top: 212px; width: 112px; }
</style>
</head>
<body>
  <section class="card card--front" aria-label="Business card front">
    <span class="brand-dot" aria-hidden="true"></span>
    <div class="brand-name">Willowbend Pharmacy</div>
    <span class="brand-rule" aria-hidden="true"></span>

    <ul class="contact-list">
      <li><svg viewBox="0 0 16 16" aria-hidden="true"><path d="M3.6 1.2l2.3 2.6-1.3 1.9c.9 2 2.6 3.7 4.7 4.7l1.9-1.3 2.6 2.3-1.3 2.6C7 14.2 1.8 9 1 3.3z"/></svg>555 214 0387</li>
      <li><svg viewBox="0 0 16 16" aria-hidden="true"><path d="M4.5 0h7A1.5 1.5 0 0 1 13 1.5v13a1.5 1.5 0 0 1-1.5 1.5h-7A1.5 1.5 0 0 1 3 14.5v-13A1.5 1.5 0 0 1 4.5 0zM5 2v10h6V2zm3 11a1 1 0 1 0 0 2 1 1 0 0 0 0-2z"/></svg>555 730 6612</li>
      <li><svg viewBox="0 0 16 16" aria-hidden="true"><path d="M1 3h14v1.2L8 8.6 1 4.2zm0 2.6l7 4.4 7-4.4V13H1z"/></svg>dorian@willowbendpharmacy.example</li>
      <li><svg viewBox="0 0 16 16" aria-hidden="true"><circle cx="8" cy="8" r="7"/></svg>willowbendpharmacy.example</li>
    </ul>

    <div class="person">
      <div class="person__name">Dorian Kessel</div>
      <div class="person__title">Pharmacy Manager</div>
    </div>
  </section>

  <section class="card card--back" aria-label="Business card back">
    <span class="brand-dot" aria-hidden="true"></span>
    <div class="brand-name">Willowbend Pharmacy</div>
    <span class="brand-rule" aria-hidden="true"></span>
  </section>
</body>
</html>
```